Corvallin Property Solutions need a business card design

Hello guys. We would need a business card design asap please.
We are a start up property investment business based in London UK specialised in buying, selling, managing and letting properties and helping distressed property owners.
The name of our Business is Corvallin, the logo symbolises the four fundamental elements of the world (earth, air, fire and water) and so it stands for strength, stability, longevity.
We would like the business card to communicate professionalism and reliability. Many many thanks indeed for your work.

Details:

1.) Marisol Dunkley
Property Investor
Mobile: +44(0)7700362517
Email: marisol.corvallin@quilbrook.example

2.) Tomas Brindle
Property Investor
Mobile: +44(0)7700845926
Email: tomas.corvallin@quilbrook.example

Industry/Entity Type

Investment

```html
<!DOCTYPE html>
<html lang="en">
<head>
<meta charset="utf-8">
<title>Corvallin Property Solutions – Business Card</title>
<link href="https://fonts.googleapis.com/css2?family=Jost:wght@400;500;600;700&display=swap" rel="stylesheet">
<style>
  :root {
    --stage: #2a2b2b;
    --card: #f7f6f6;
    --card-shade: #e4e1e0;
    --ink: #161616;
    --blue: #2c4fa3;
    --green: #1f8a3c;
    --red: #d3262a;
    --web-red: #c4241f;
  }
  * { box-sizing: border-box; margin: 0; padding: 0; }
  html, body {
    width: 1000px; height: 1200px; overflow: hidden;
    background: var(--stage);
    font-family: "Jost", "Futura", sans-serif;
    color: var(--ink);
  }
  .canvas { position: relative; width: 1000px; height: 1200px; }
  .card {
    position: absolute;
    width: 669px; height: 432px;
    background: var(--card);
    overflow: hidden;
  }
  .card--front { left: 144px; top: 95px; }
  .card--back { left: 155px; top: 651px; }
  .card__texture {
    position: absolute; inset: 0;
    background:
      radial-gradient(ellipse at 55% 45%, #ffffff 0%, rgba(255,255,255,0) 60%),
      linear-gradient(135deg, var(--card-shade) 0%, var(--card) 45%, var(--card-shade) 100%);
  }
  .brand {
    position: absolute;
    display: flex; flex-direction: column; align-items: center;
    color: var(--ink); font-weight: 600; text-transform: uppercase;
    text-align: center;
  }
  .brand__mark {
    width: 54px; height: 54px; background: var(--ink);
    margin-bottom: 22px;
  }
  .brand__name { font-size: 27px; letter-spacing: 0.5px; line-height: 1; }
  .brand__tagline { font-size: 12px; letter-spacing: 0.3px; margin-top: 8px; line-height: 1; }
  .card--front .brand { left: 48px; top: 96px; width: 182px; }
  .card--back .brand { left: 0; right: 0; top: 88px; }

  .contact {
    position: absolute; right: 48px; top: 186px;
    text-align: right;
  }
  .contact__name { font-size: 21px; font-weight: 600; letter-spacing: 0.6px; text-transform: uppercase; line-height: 1; }
  .contact__role { font-size: 15px; font-weight: 600; color: var(--blue); text-transform: uppercase; margin-top: 8px; margin-right: 8px; line-height: 1; }
  .contact__line {
    display: flex; justify-content: flex-end; align-items: center; gap: 6px;
    font-size: 18px; font-weight: 400; line-height: 1; margin-top: 14px;
  }
  .contact__line:first-of-type { margin-top: 18px; }
  .contact__icon { width: 22px; height: 22px; flex: none; }

  .address {
    position: absolute; left: 0; right: 0; top: 223px;
    text-align: center; font-size: 21px; line-height: 1.3; font-weight: 400;
  }
  .website {
    position: absolute; left: 0; right: 0; top: 333px;
    text-align: center; font-size: 20px; font-weight: 600; color: var(--web-red);
  }
</style>
</head>
<body>
<main class="canvas">

  <section class="card card--front" aria-label="Business card front">
    <div class="card__texture" role="img" aria-label="Soft light grey faceted background pattern"></div>
    <div class="brand">
      <span class="brand__mark"></span>
      <span class="brand__name">Corvallin</span>
      <span class="brand__tagline">Property Solutions</span>
    </div>
    <div class="contact">
      <p class="contact__name">Marisol Dunkley</p>
      <p class="contact__role">Property Investor</p>
      <p class="contact__line">+44(0)7700362517
        <svg class="contact__icon" viewBox="0 0 22 22" aria-hidden="true">
          <rect x="6" y="1" width="11" height="20" rx="2" fill="none" stroke="var(--green)" stroke-width="2"/>
          <rect x="8.5" y="4" width="6" height="11" fill="var(--green)" opacity=".35"/>
          <circle cx="11.5" cy="18" r="1.1" fill="var(--green)"/>
        </svg>
      </p>
      <p class="contact__line">marisol.corvallin@quilbrook.example
        <svg class="contact__icon" viewBox="0 0 22 22" aria-hidden="true">
          <rect x="1" y="5" width="20" height="13" fill="var(--red)"/>
          <path d="M1 5 L11 12.5 L21 5 M1 18 L8.5 11 M21 18 L13.5 11" fill="none" stroke="#fff" stroke-width="1.5"/>
        </svg>
      </p>
    </div>
  </section>

  <section class="card card--back" aria-label="Business card back">
    <div class="card__texture" role="img" aria-label="Soft light grey faceted background pattern"></div>
    <div class="brand">
      <span class="brand__mark"></span>
      <span class="brand__name">Corvallin</span>
      <span class="brand__tagline">Property Solutions</span>
    </div>
    <p class="address">27 Harrowfield Lane BRAMLEIGH<br>TD9 4QX</p>
    <p class="website">www.corvallin.com</p>
  </section>

</main>
</body>
</html>
```